Cannabis vape brand needs new packaging

We are a cannabis brand "k7" We will create products in all product categories according to cannabis.
-Vapes
-Edibles
-Capsules
-Roll-ons
-Pre-rolls
-Disposables
Please provide a vape box sample design
Our goal is to target all age groups and vendors. We feel that the cannabis industry for the most parts caters to younger population. I have provided some brands that check all the boxes for me that we would like to use as inspiration
-Quiet Meadow
-Tumo Sweetworks

Target Market(s)

We are looking to target all age groups and genders

Industry/Entity Type

Cannabis / Retail

Requirements
Nice to have
• I would like to see more packaging like the inspiration shared. Remember we are targetting all audience male and female. I feel like quiet meadow does this great. Please pay close attention to inspiration

```html
<!DOCTYPE html>
<html lang="en">
<head>
<meta charset="utf-8">
<title>k7 Blueberry Vape Box</title>
<link rel="stylesheet" href="https://fonts.googleapis.com/css2?family=Oswald:wght@300;600&family=Poppins:wght@700&display=swap">
<style>
  :root {
    --stage: #e4e4e6;
    --label-navy: #1a1845;
    --paper: #f4f4f4;
    --band: #e6e6e6;
    --ink: #0d0d0d;
    --pink: #de3aa3;
    --blue: #3a3be0;
    --deep-blue: #0f2a8f;
    --white: #ffffff;
  }
  * { margin: 0; padding: 0; box-sizing: border-box; }
  html, body { width: 1200px; height: 983px; overflow: hidden; }
  body {
    background: var(--stage);
    display: flex;
    align-items: center;
    justify-content: center;
  }
  .box-net {
    display: flex;
    gap: 16px;
    align-items: stretch;
    height: 600px;
  }

  /* End panel */
  .end-panel {
    width: 190px;
    background: var(--paper);
    border-radius: 10px;
    box-shadow: 0 10px 30px rgba(0,0,0,0.12);
    display: flex;
    align-items: center;
    justify-content: center;
    gap: 22px;
  }
  .end-panel__text {
    writing-mode: vertical-rl;
    font-family: "Oswald", sans-serif;
    font-size: 20px;
    text-transform: uppercase;
    color: var(--ink);
    letter-spacing: 0.5px;
    white-space: nowrap;
  }
  .end-panel__text .light { font-weight: 300; }
  .end-panel__text .bold { font-weight: 600; }
  .end-panel__mark {
    writing-mode: vertical-rl;
    display: flex;
    align-items: center;
    gap: 10px;
  }
  .end-panel__mark .brand-mark__square { width: 22px; height: 22px; }
  .end-panel__mark .brand-mark__name { font-size: 72px; }

  /* Lid */
  .box-lid {
    width: 934px;
    display: flex;
    box-shadow: 0 10px 30px rgba(0,0,0,0.12);
  }
  .end-cap { width: 30px; background: var(--paper); }
  .end-cap--left { border-radius: 10px 0 0 10px; }
  .end-cap--right { border-radius: 0 10px 10px 0; }
  .pattern-panel {
    flex: 1;
    position: relative;
    background: linear-gradient(135deg, var(--pink) 0%, var(--blue) 35%, var(--deep-blue) 55%, var(--pink) 80%, var(--blue) 100%);
  }
  .pattern-panel--right {
    background: linear-gradient(225deg, var(--blue) 0%, var(--pink) 30%, var(--deep-blue) 55%, var(--pink) 78%, var(--blue) 100%);
  }
  .center-band {
    width: 270px;
    background: var(--band);
    display: flex;
    flex-direction: column;
    align-items: center;
    padding-top: 70px;
  }
  .brand-mark {
    display: flex;
    align-items: center;
    gap: 14px;
  }
  .brand-mark__square {
    width: 34px;
    height: 34px;
    background: var(--ink);
  }
  .brand-mark__name {
    font-family: "Oswald", sans-serif;
    font-weight: 600;
    font-size: 110px;
    line-height: 1;
    color: var(--ink);
  }
  .product-type {
    margin-top: 36px;
    text-align: center;
    font-family: "Oswald", sans-serif;
    color: var(--ink);
    text-transform: uppercase;
    line-height: 1.05;
  }
  .product-type__category { font-weight: 300; font-size: 30px; letter-spacing: 1px; }
  .product-type__device { font-weight: 600; font-size: 40px; }
  .volume-tag {
    margin-top: 70px;
    background: var(--ink);
    color: var(--white);
    font-family: "Oswald", sans-serif;
    font-weight: 300;
    font-size: 36px;
    line-height: 1;
    padding: 6px 16px 8px;
  }
  .flavour-label {
    background: var(--label-navy);
    color: var(--white);
    font-family: "Poppins", sans-serif;
    font-weight: 700;
    font-size: 28px;
    letter-spacing: 1px;
    padding: 24px 28px;
    border-radius: 10px;
  }
  .warning-badge {
    position: absolute;
    right: 28px;
    bottom: 70px;
    width: 76px;
    height: 68px;
  }
</style>
</head>
<body>
  <main class="box-net">
    <aside class="end-panel">
      <div class="end-panel__text"><span class="light">Cannabis</span> <span class="bold">Vaping Device</span></div>
      <div class="brand-mark end-panel__mark">
        <span class="brand-mark__square"></span>
        <span class="brand-mark__name">k7</span>
      </div>
    </aside>
    <section class="box-lid">
      <div class="end-cap end-cap--left"></div>
      <div class="pattern-panel" role="img" aria-label="Flowing pink and blue topographic wave pattern"></div>
      <div class="center-band">
        <div class="brand-mark">
          <span class="brand-mark__square"></span>
          <span class="brand-mark__name">k7</span>
        </div>
        <div class="product-type">
          <div class="product-type__category">Cannabis</div>
          <div class="product-type__device">Vaping<br>Device</div>
        </div>
        <div class="volume-tag">2ml</div>
        <div class="flavour-label">BLUEBERRY</div>
      </div>
      <div class="pattern-panel pattern-panel--right" role="img" aria-label="Flowing pink and blue topographic wave pattern">
        <svg class="warning-badge" viewBox="0 0 80 72" aria-hidden="true">
          <path d="M40 4 L76 68 L4 68 Z" fill="#ffffff" stroke="#0d0d0d" stroke-width="5" stroke-linejoin="round"/>
        </svg>
      </div>
      <div class="end-cap end-cap--right"></div>
    </section>
  </main>
</body>
</html>
```